Trucking company needs business card design

New trucking company needs fresh ideas on a business card. Contracted exclusively to Parcelwing, can incorporate their colors or style, but not necessary.
Beckley Haulage, Inc (with or without the Inc.)
Dale Quimby, CEO
801-555-0174
PO BOX 672
Lehi, UT

Need to add my email address to the card--beckleyhaulageinc@quillpost.net

Trucking Company

```html
<!DOCTYPE html>
<html lang="en">
<head>
<meta charset="utf-8">
<title>Beckley Haulage – Business Card</title>
<link href="https://fonts.googleapis.com/css2?family=Source+Sans+3:wght@400;600&display=swap" rel="stylesheet">
<style>
  :root {
    --backdrop: #e8e4de;
    --card-white: #ffffff;
    --card-black: #0e0e0e;
    --ink: #1a1a1a;
    --ink-soft: #4a4a4a;
    --accent: #ef7a45;
    --reverse: #ffffff;
  }
  * { box-sizing: border-box; margin: 0; padding: 0; }
  html, body {
    width: 1200px; height: 1023px; overflow: hidden;
    background: var(--backdrop);
    font-family: "Source Sans 3", Arial, sans-serif;
  }
  .sheet {
    width: 1200px; height: 1023px;
    display: flex; flex-direction: column;
    align-items: center; justify-content: center; gap: 60px;
  }
  .card {
    width: 630px; height: 360px;
    position: relative;
    box-shadow: 0 6px 18px rgba(0,0,0,0.18);
  }
  .card--front { background: var(--card-white); padding: 48px 54px; }
  .card--back {
    background: var(--card-black);
    display: flex; align-items: center; justify-content: center;
  }
  .brand { display: flex; align-items: center; gap: 18px; }
  .brand__mark { width: 54px; height: 54px; background: var(--accent); flex: none; }
  .brand__name {
    font-size: 42px; font-weight: 600; color: var(--ink);
    letter-spacing: 0.5px; line-height: 1;
  }
  .card--back .brand__mark { background: var(--reverse); width: 70px; height: 70px; }
  .card--back .brand__name { color: var(--reverse); font-size: 50px; }
  .person { margin-top: 56px; }
  .person__name {
    font-size: 27px; font-weight: 600; color: var(--accent);
    letter-spacing: 0.5px; line-height: 1.1;
  }
  .person__role { font-size: 19px; color: var(--ink-soft); margin-top: 4px; }
  .contacts { list-style: none; margin-top: 26px; }
  .contacts li {
    display: flex; align-items: center; gap: 12px;
    font-size: 19px; color: var(--ink-soft); line-height: 1.55;
  }
  .contacts__icon { width: 17px; height: 17px; flex: none; }
  .contacts__spacer { width: 17px; flex: none; }
</style>
</head>
<body>
  <main class="sheet">
    <section class="card card--front">
      <div class="brand">
        <span class="brand__mark"></span>
        <span class="brand__name">Beckley Haulage</span>
      </div>
      <div class="person">
        <p class="person__name">DALE QUIMBY</p>
        <p class="person__role">CEO</p>
      </div>
      <ul class="contacts">
        <li>
          <svg class="contacts__icon" viewBox="0 0 17 17" aria-hidden="true">
            <rect width="17" height="17" rx="2" fill="var(--accent)"/>
            <path d="M5 4.5 L7 4.5 L7.8 7 L6.7 7.8 Q7.6 9.7 9.3 10.4 L10.1 9.3 L12.5 10.1 L12.5 12 Q8.5 12.6 6 10 Q4.4 7.8 5 4.5Z" fill="#fff"/>
          </svg>
          801-555-0174
        </li>
        <li>
          <svg class="contacts__icon" viewBox="0 0 17 17" aria-hidden="true">
            <rect width="17" height="17" rx="2" fill="var(--accent)"/>
            <rect x="3.5" y="5" width="10" height="7" fill="none" stroke="#fff" stroke-width="1.2"/>
            <path d="M3.5 5 L8.5 9 L13.5 5" fill="none" stroke="#fff" stroke-width="1.2"/>
          </svg>
          beckleyhaulageinc@quillpost.net
        </li>
        <li><span class="contacts__spacer"></span>PO BOX 672, Lehi, UT</li>
      </ul>
    </section>

    <section class="card card--back">
      <div class="brand">
        <span class="brand__mark"></span>
        <span class="brand__name">Beckley Haulage</span>
      </div>
    </section>
  </main>
</body>
</html>
```